Business card New design- upscale

Looking for modern design business cards. Minimalist, mix of gloss and matte finishes. Texas based Contractor company doing Mechanical hvac and plumbing, focused on commercial and industrial manufacturing facilities. We don't hand too many out so high end materials or functionality...will be considered. Please see attached files for info needed on cards. *New plumbing license needs to be edited to say M82716. Www.polvaxgroup.com
P.s. Website will also be redesigned soon.

Target Market(s)

Facility managers for commercial buildings, mechanical engineers for industrial manufacturing facilities including pharmaceutical, semiconductor, food & beverage, etc

Contact Information for Business Card

See attached images

Requirements
Must have
• All Logo colors: purple, black and Gray. 1, 2 or 4 rounded corners. All content on existing business cards (see attached images).
Nice to have
• Matte and gloss print. Embossing, raised print, functionality.
Should not have
• Stock images, generic construction.

```html
<!DOCTYPE html>
<html lang="en">
<head>
<meta charset="utf-8">
<title>Polvax Group business card</title>
<link href="https://fonts.googleapis.com/css2?family=Montserrat:wght@400;500;600;700&display=swap" rel="stylesheet">
<style>
  :root {
    --bg: #e9e7ee;
    --purple: #3d2266;
    --purple-light: #53357f;
    --purple-faint: #4b2e77;
    --ink: #ffffff;
  }
  html, body {
    margin: 0;
    padding: 0;
    width: 1200px;
    height: 881px;
    overflow: hidden;
    background: var(--bg);
    font-family: "Montserrat", sans-serif;
  }
  .canvas {
    position: relative;
    width: 1200px;
    height: 881px;
  }
  .card {
    position: absolute;
    left: 290px;
    width: 620px;
    height: 354px;
    border-radius: 26px;
    background: linear-gradient(100deg, var(--purple) 0%, var(--purple-light) 32%, var(--purple) 46%, var(--purple) 100%);
    box-shadow: 0 10px 28px rgba(30, 10, 60, 0.28);
    overflow: hidden;
    color: var(--ink);
  }
  .card-front { top: 48px; }
  .card-back { top: 472px; }

  .front-brand {
    position: absolute;
    left: 0; right: 0; top: 0; bottom: 0;
    display: flex;
    align-items: center;
    justify-content: center;
    gap: 16px;
  }
  .brand-mark {
    width: 30px;
    height: 30px;
    background: var(--purple-faint);
  }
  .brand-name {
    font-weight: 500;
    font-size: 46px;
    letter-spacing: 6px;
    color: var(--purple-faint);
    text-transform: uppercase;
  }

  .back-brand {
    position: absolute;
    left: 40px;
    top: 34px;
    display: flex;
    align-items: center;
    gap: 10px;
  }
  .back-brand .brand-mark { width: 18px; height: 18px; }
  .back-brand .brand-name { font-size: 26px; letter-spacing: 4px; }

  .contact-block {
    position: absolute;
    left: 30px;
    top: 96px;
    bottom: 24px;
    padding-left: 18px;
    border-left: 1.5px solid var(--ink);
  }
  .person-name {
    margin: 0;
    font-weight: 700;
    font-size: 30px;
    letter-spacing: 2px;
    text-transform: uppercase;
    line-height: 1.1;
  }
  .person-title {
    margin: 4px 0 10px;
    font-weight: 600;
    font-size: 15px;
    line-height: 1.25;
  }
  .contact-list {
    list-style: none;
    margin: 0 0 12px;
    padding: 0;
    font-weight: 500;
    font-size: 14.5px;
    line-height: 1.4;
  }
  .contact-list li { display: flex; align-items: center; gap: 8px; }
  .contact-list svg { width: 12px; height: 12px; flex: none; }
  .services {
    margin: 0;
    font-weight: 700;
    font-size: 15px;
    line-height: 1.3;
  }

  .license-block {
    position: absolute;
    right: 22px;
    top: 22px;
    width: 230px;
    padding-right: 12px;
    border-right: 1.5px solid var(--ink);
    text-align: right;
    font-weight: 600;
    font-size: 11.5px;
    line-height: 1.32;
  }
  .license-block p { margin: 0; }
  .license-site {
    position: absolute;
    right: 34px;
    bottom: 60px;
    font-weight: 600;
    font-size: 13px;
  }
</style>
</head>
<body>
<div class="canvas">

  <section class="card card-front" aria-label="Card front">
    <div class="front-brand">
      <span class="brand-mark"></span>
      <span class="brand-name">Polvax Group</span>
    </div>
  </section>

  <section class="card card-back" aria-label="Card back">
    <div class="back-brand">
      <span class="brand-mark"></span>
      <span class="brand-name">Polvax Group</span>
    </div>

    <div class="contact-block">
      <h1 class="person-name">Dale Brenner</h1>
      <p class="person-title">Lead Estimator/Sr.<br>Project Manager</p>
      <ul class="contact-list">
        <li>
          <svg viewBox="0 0 12 12" fill="none" stroke="#fff" stroke-width="1.2"><rect x="3" y="1" width="6" height="10" rx="1"/><line x1="5" y1="9.3" x2="7" y2="9.3"/></svg>
          (520) 555-0147
        </li>
        <li>
          <svg viewBox="0 0 12 12" fill="#fff"><path d="M2.5 1.5l2 0.3 0.6 2.2-1.2 1a6 6 0 0 0 3.1 3.1l1-1.2 2.2 0.6 0.3 2-1.3 1C5 10.3 1.7 7 1.5 2.8z"/></svg>
          (817) 555-0192
        </li>
        <li>
          <svg viewBox="0 0 12 12" fill="none" stroke="#fff" stroke-width="1.1"><rect x="1" y="2.5" width="10" height="7"/><polyline points="1,2.5 6,6.5 11,2.5"/></svg>
          dbrenner@polvaxgroup.com
        </li>
        <li>
          <svg viewBox="0 0 12 12" fill="none" stroke="#fff" stroke-width="1"><circle cx="6" cy="6" r="5"/><ellipse cx="6" cy="6" rx="2.2" ry="5"/><line x1="1" y1="6" x2="11" y2="6"/></svg>
          www.polvaxgroup.com
        </li>
      </ul>
      <p class="services">Commercial &amp; Industrial Contractors<br>Mechanical &amp; Plumbing Services</p>
    </div>

    <div class="license-block">
      <p>M-82716 Regulated by<br>the Texas State Board of<br>Plumbing Examiners,<br>P.O. Box 3100,<br>Austin, TX. 78760;<br>1-800-555-0134,<br>512-555-0180 /<br>TACLA52018C<br>Regulated by the Texas<br>Department of Licensing and<br>Regulation, P.O. Box 10440,<br>Austin, TX. 78712;<br>1-800-555-0166,<br>512-555-0123</p>
    </div>
    <div class="license-site">www.license.example.tx.us</div>
  </section>

</div>
</body>
</html>
```